Post it Note design

POST-IT NOTE DESIGN (CONTENT)
Size recommended: 4x6 for handwriting space.
Header (Bold):
Lighting Issue Detected on Your Property
Sub-header:
During our routine night inspection, we noted the following item(s):
Checkbox List:
⬜ Building Lights Out
⬜ Pole Lights Out
⬜ Sign Not Illuminated
⬜ Other ________________________
Action Line:
We can provide a quote or dispatch service right away.
Area for notes
Contact Block (Bold & Centered):
Brovane Fixture Inc.
Service@BrovaneFixture.com
www.BrovaneFixture.com
877-514-0862
Industry/Entity Type
Electrical lighting
Colors
Designer to choose colors to be used in the design.
Look and feel
Each slider illustrates characteristics of the customer's brand and the style your logo design should communicate.

```html
<!DOCTYPE html>
<html lang="en">
<head>
<meta charset="utf-8">
<title>Lighting Issue Notes – Brovane Fixture Inc.</title>
<link rel="stylesheet" href="https://fonts.googleapis.com/css2?family=Bebas+Neue&family=Roboto+Condensed:ital,wght@0,400;0,500;0,700;1,400;1,500&display=swap">
<style>
:root{
  --navy:#0b1a8a;
  --red:#d3172a;
  --ink:#1c1c1c;
  --rule:#d6d6d6;
  --paper:#ffffff;
  --stage:#2e2e2e;
}
*{margin:0;padding:0;box-sizing:border-box}
html,body{width:1200px;height:960px;overflow:hidden;background:var(--stage)}
body{position:relative;font-family:"Roboto Condensed",sans-serif;color:var(--ink)}
.note{position:absolute;top:102px;width:490px;height:735px;background:var(--paper);overflow:hidden}
.note--swoosh{left:82px}
.note--ruled{left:613px}
.abs{position:absolute}
.headline{font-family:"Bebas Neue",sans-serif;color:#fff;line-height:.98;letter-spacing:-.5px}
.note--swoosh .headline{left:28px;top:24px;font-size:50px;text-shadow:2px 2px 0 var(--red)}
.question{left:405px;top:14px;font-family:"Bebas Neue",sans-serif;font-size:110px;color:#2a3aa6;opacity:.75}
.brand-oval{left:262px;top:101px;width:200px;height:87px;border:2px solid var(--red);border-radius:50%;background:#fff;display:flex;align-items:center;justify-content:center}
.brand-name{font-weight:700;color:var(--navy);font-size:22px;line-height:1;text-align:center}
.lede{font-size:24px;font-weight:500;line-height:1.05;color:#222}
.note--swoosh .lede{left:28px;top:200px}
.checks{list-style:none;font-size:17px;font-weight:500}
.checks li{display:flex;align-items:center;gap:9px}
.box{width:13px;height:13px;border:1.5px solid #222;flex:none}
.note--swoosh .checks{display:grid;grid-template-columns:185px auto;row-gap:6px;left:28px;top:264px}
.action-pill{left:27px;top:324px;width:436px;height:25px;border:2px solid var(--red);border-radius:13px;font-style:italic;font-size:16px;font-weight:500;display:flex;align-items:center;justify-content:center}
.notes-label{left:28px;top:365px;color:var(--red);font-size:17px;font-weight:500}
.photo{background:linear-gradient(180deg,#f6f6f7,#e9eaec)}
.note--swoosh .photo{left:21px;top:388px;width:449px;height:282px;opacity:.7}
.footer{left:0;width:490px;background:var(--navy);color:#fff;text-align:center;border-bottom:7px solid var(--red)}
.note--swoosh .footer{top:685px;height:50px;padding-top:8px}
.note--ruled .footer{top:675px;height:60px;padding-top:12px}
.footer strong{display:block;font-size:13.5px;font-weight:700;margin-bottom:3px}
.footer span{font-size:13px}
.note--ruled .header{left:0;top:0;width:490px;height:154px;background:var(--navy)}
.note--ruled .headline{left:0;top:30px;width:490px;text-align:center;font-size:58px;line-height:.92}
.hot{color:var(--red)}
.note--ruled .lede{left:30px;top:182px;font-size:22px}
.note--ruled .checks{left:30px;top:303px;display:grid;row-gap:8px;font-size:16.5px}
.note--ruled .box{border-color:var(--red)}
.action-spaced{left:30px;top:412px;font-style:italic;font-weight:500;font-size:16px;letter-spacing:1.6px;line-height:1}
.note--ruled .photo{left:21px;top:474px;width:181px;height:100px}
.note--ruled .brand-name{position:absolute;left:20px;top:600px;width:180px;font-size:24px}
.ruled-lines{left:217px;top:191px;width:241px}
</style>
</head>
<body>

<section class="note note--swoosh">
  <svg class="abs" style="left:0;top:0" width="490" height="220" viewBox="0 0 490 220" aria-hidden="true">
    <path d="M0 0H490V155C400 140 330 128 250 128C150 128 60 140 0 152Z" fill="var(--navy)"/>
    <path d="M250 128C330 128 420 138 490 150V165C430 150 330 138 250 128Z" fill="var(--red)"/>
    <path d="M470 146L490 150V196C480 180 470 160 440 140Z" fill="var(--red)"/>
  </svg>
  <div class="abs question" aria-hidden="true">?</div>
  <h1 class="abs headline">Lighting Issue Detected<br>On Your Property</h1>
  <div class="abs brand-oval"><span class="brand-name">Brovane Fixture</span></div>
  <p class="abs lede">During our routine night inspection,<br>we noted the following item(s):</p>
  <ul class="abs checks">
    <li><span class="box"></span>Building Lights Out</li>
    <li><span class="box"></span>Sign Not Illuminated</li>
    <li><span class="box"></span>Pole Lights Out</li>
    <li><span class="box"></span>Other</li>
  </ul>
  <p class="abs action-pill">We can provide a quote or dispatch service right away.</p>
  <p class="abs notes-label">Notes</p>
  <div class="abs photo" role="img" aria-label="Faded photo of the company's white service van behind the notes area"></div>
  <footer class="abs footer">
    <strong>Brovane Fixture Inc.</strong>
    <span>Service@BrovaneFixture.com &nbsp;|&nbsp; www.BrovaneFixture.com &nbsp;|&nbsp; 877-514-0862</span>
  </footer>
</section>

<section class="note note--ruled">
  <div class="abs header"></div>
  <h1 class="abs headline">Lighting Issue <span class="hot">Detected</span><br><span class="hot">On Your</span> Property</h1>
  <p class="abs lede">During our routine<br>night inspection,<br>we noted the<br>following item(s):</p>
  <ul class="abs checks">
    <li><span class="box"></span>Building Lights Out</li>
    <li><span class="box"></span>Pole Lights Out</li>
    <li><span class="box"></span>Sign Not Illuminated</li>
    <li><span class="box"></span>Other</li>
  </ul>
  <p class="abs action-spaced">We can provide a<br>quote or dispatch<br>service right away.</p>
  <div class="abs photo" role="img" aria-label="Photo of a white bucket truck with safety cones"></div>
  <span class="brand-name">Brovane Fixture</span>
  <svg class="abs ruled-lines" width="241" height="460" viewBox="0 0 241 460" aria-hidden="true">
    <g stroke="var(--rule)" stroke-width="1.5">
      <line x1="0" y1="1" x2="241" y2="1"/><line x1="0" y1="31" x2="241" y2="31"/>
      <line x1="0" y1="61" x2="241" y2="61"/><line x1="0" y1="92" x2="241" y2="92"/>
      <line x1="0" y1="122" x2="241" y2="122"/><line x1="0" y1="152" x2="241" y2="152"/>
      <line x1="0" y1="183" x2="241" y2="183"/><line x1="0" y1="213" x2="241" y2="213"/>
      <line x1="0" y1="243" x2="241" y2="243"/><line x1="0" y1="273" x2="241" y2="273"/>
      <line x1="0" y1="304" x2="241" y2="304"/><line x1="0" y1="334" x2="241" y2="334"/>
      <line x1="0" y1="364" x2="241" y2="364"/><line x1="0" y1="395" x2="241" y2="395"/>
      <line x1="0" y1="425" x2="241" y2="425"/><line x1="0" y1="455" x2="241" y2="455"/>
    </g>
  </svg>
  <footer class="abs footer">
    <strong>Brovane Fixture Inc.</strong>
    <span>Service@BrovaneFixture.com &nbsp;|&nbsp; www.BrovaneFixture.com &nbsp;|&nbsp; 877-514-0862</span>
  </footer>
</section>

</body>
</html>
```